Photographer's price list

I am a photographer who runs a studio (Pinefield Studio) and need to have a document to send clients detailing my packages (collections) and prices. I have written the text in a word document and need a designer to lay it out for me using my logo and two specific fonts: DejaVu Sans and LainieDaySH.

The look should be clean and modern and keep in the same style as my logo. I will primarily be using the final product as a PDF file to email to potential clients. It should stay black and white.

I would also like to be able to update the text myself as my prices and packages change. So I would like a PSD file.

I think I would like for the document to be in landscape format with "Collections" on one side and A la Carte on the other, but I am open to other ideas.

As for sizing, it should be a standard size so that clients can print it out if they like.

Requirements
Must have
• my logo
fonts: DejaVu and LainieDaySH
Easy to email
Easy to display on one page upon opening
Standard size so that printing from a home computer is easy to do.

```html
<!DOCTYPE html>
<html lang="en">
<head>
<meta charset="utf-8">
<title>Pinefield Studio – 2013 Photography Collections</title>
<link href="https://fonts.googleapis.com/css2?family=Didact+Gothic&family=Fjalla+One&family=Pathway+Gothic+One&family=Questrial&display=swap" rel="stylesheet">
<style>
:root{
  --backdrop:#7a4a2a;
  --ink:#231f20;
  --paper:#ffffff;
  --mist:#e3e4e6;
  --silver:#bfc0c2;
  --grey-text:#7a7a7a;
  --light-text:#f2f2f2;
}
*{box-sizing:border-box;margin:0;padding:0}
html,body{width:1200px;height:855px;overflow:hidden;background:var(--backdrop)}
.sheet{position:relative;width:1200px;height:855px}
.page{position:absolute;overflow:hidden}
.label{position:absolute;width:540px;text-align:center;font-family:"Questrial",sans-serif;font-size:28px;letter-spacing:3px;color:var(--paper)}

/* back page */
.back{left:60px;top:7px;width:540px;height:380px;background:var(--paper)}
.back .band{position:absolute;left:0;top:132px;width:540px;height:111px;background:var(--ink)}
.logo-disc{position:absolute;border-radius:50%;background:var(--paper);display:flex;align-items:center;justify-content:center;text-align:center;font-family:"Didact Gothic",sans-serif;color:var(--ink);letter-spacing:2px}
.back .logo-disc{left:24px;top:118px;width:148px;height:148px;border:4px solid var(--silver);font-size:15px;line-height:1.3}
.about{position:absolute;left:205px;top:146px;width:205px;color:var(--light-text);font-family:"Didact Gothic",sans-serif}
.about h2{font-weight:400;font-size:11px;margin-bottom:5px}
.about p{font-size:6px;line-height:1.35;margin-bottom:5px}
.web{position:absolute;left:35px;top:268px;font-family:"Didact Gothic",sans-serif;font-size:8px;letter-spacing:2px;color:var(--ink)}

/* front page */
.front{left:600px;top:7px;width:540px;height:380px;background:var(--ink)}
.front .strip{position:absolute;left:0;top:0;width:540px;height:9px;background:var(--silver)}
.photo{position:absolute;left:0;top:12px;width:373px;height:258px;background:linear-gradient(135deg,#e8e8e8,#8c8c8c 55%,#3a3a3a)}
.ribbon{position:absolute;left:410px;top:12px;width:93px;height:150px;background:var(--silver)}
.front .logo-disc{left:413px;top:121px;width:88px;height:88px;border:3px solid var(--silver);font-size:9px;line-height:1.3}
.year{position:absolute;right:30px;top:240px;font-family:"Fjalla One",sans-serif;font-size:56px;color:var(--paper);line-height:1}
.title{position:absolute;left:17px;top:305px;font-family:"Fjalla One",sans-serif;font-size:46px;color:var(--paper);line-height:1;letter-spacing:1.4px;white-space:nowrap}

/* inside page 1 */
.inside-one{left:60px;top:433px;width:542px;height:382px;background:var(--mist);font-family:"Didact Gothic",sans-serif;color:var(--grey-text)}
.inside-one h2{position:absolute;left:24px;top:42px;font-weight:400;font-size:25px;color:var(--ink)}
.includes{position:absolute;left:24px;top:81px;width:505px;font-size:7.4px;line-height:2}
.collection{position:absolute;width:225px}
.collection h3{font-weight:400;font-size:23px;color:var(--ink);margin-bottom:6px;white-space:nowrap}
.collection p{font-family:"Pathway Gothic One",sans-serif;font-size:7.5px;line-height:1.45;margin-bottom:4px}
.c1{left:24px;top:148px}.c3{left:274px;top:148px}
.c2{left:24px;top:226px}.c4{left:274px;top:226px}
.bubbles-light{position:absolute;left:0;top:314px;width:542px;height:62px;background:linear-gradient(180deg,rgba(200,200,202,0),#c9cacc 50%,rgba(200,200,202,0))}

/* inside page 2 */
.inside-two{left:602px;top:433px;width:540px;height:382px;background:var(--ink);color:var(--light-text)}
.bubbles-dark{position:absolute;left:0;width:540px;height:62px;background:linear-gradient(180deg,rgba(80,80,80,0),#4a4a4a 50%,rgba(80,80,80,0))}
.bubbles-dark.top{top:3px}.bubbles-dark.bottom{top:310px}
.item{position:absolute;width:248px}
.item h3{font-family:"Didact Gothic",sans-serif;font-weight:400;font-size:12px;line-height:1.2;margin-bottom:6px;white-space:nowrap}
.item p{font-family:"Pathway Gothic One",sans-serif;font-size:7.8px;line-height:1.4}
.l1{left:28px;top:97px}.l2{left:28px;top:166px}.l3{left:28px;top:241px}
.r1{left:269px;top:80px}.r2{left:269px;top:130px}.r3{left:269px;top:183px}.r4{left:269px;top:240px}
</style>
</head>
<body>
<div class="sheet">

  <section class="page back">
    <div class="band"></div>
    <div class="logo-disc">PINEFIELD<br>STUDIO</div>
    <div class="about">
      <h2>About us</h2>
      <p>Pinefield Studio, based in Lyon, France, is a newly launched studio led by independent photographer Clara Wendt. She specializes in portrait, children and cause-related photography, and is currently working on a collection featuring mothers and children.</p>
      <p>Clara holds a Master's in Visual Arts from Harwell University, and a BA from Linden College. She is available for assignments worldwide.</p>
    </div>
    <div class="web">www.pinefieldstudio.com</div>
  </section>
  <div class="label" style="left:60px;top:390px">BACK PAGE</div>

  <section class="page front">
    <div class="strip"></div>
    <div class="photo" role="img" aria-label="Black and white portrait photograph of three children"></div>
    <div class="ribbon"></div>
    <div class="logo-disc">PINEFIELD<br>STUDIO</div>
    <div class="year">2013</div>
    <div class="title">PHOTOGRAPHY COLLECTIONS</div>
  </section>
  <div class="label" style="left:600px;top:390px">FRONT PAGE</div>

  <section class="page inside-one">
    <h2>All collections&nbsp; include:</h2>
    <div class="includes">One to two hour portrait session with photographer in location of your choice<br>(unlimited time if necessary!)<br>Clara will create a presentation video with hand-selected music and custom editing, which tells your story, highlights the best images, and reveals the connections within your family. An online gallery for viewing and ordering helps you share your images with family and friends.</div>
    <div class="collection c1"><h3>Collection 1: 300 €</h3><p>Your favorite five images from the session will be professionally edited and presented to you on disk as high resolution jpegs</p></div>
    <div class="collection c3"><h3>Collection 3: 500 €</h3><p>Your favorite fifteen images from the session will be professionally edited and presented to you on disk as high resolution jpegs<br>Your favorite two images from the session will be professionally printed for you (20x30cm) on Ashfield paper, Clara's favorite for portraits.</p></div>
    <div class="collection c2"><h3>Collection 2: 400 €</h3><p>Your favorite ten images from the session will be professionally edited and given to you on disk as high resolution jpegs<br>Your favorite image from the session will be professionally printed for you (20x30cm) on Ashfield paper, Clara's favorite for portraits.</p></div>
    <div class="collection c4"><h3>Collection 4: 600 €</h3><p>ALL presented images from the session will be professionally edited and presented to you on disk as high resolution jpegs (approximately 40+ images)</p><p>Your favorite two images from the session will be professionally printed for you (20x30cm) on Ashfield paper, Clara's favorite for portraits.</p></div>
    <div class="bubbles-light" role="img" aria-label="Decorative band of soft grey bubbles"></div>
  </section>
  <div class="label" style="left:61px;top:813px">INSIDE PAGE 1</div>

  <section class="page inside-two">
    <div class="bubbles-dark top" role="img" aria-label="Decorative band of translucent bubbles"></div>
    <div class="item l1"><h3>A LA CARTE</h3><p>These products may be purchased separately to complement your collection. A consultation with Clara will help you decide which products are best for gifts and for your home.</p></div>
    <div class="item l2"><h3>A LA CARTE - 25 € EACH<br>HIGH RESOLUTION DIGITAL IMAGES</h3><p>Perfect if you just need to add "one more image" to your collection!<br>High-resolution jpeg file</p></div>
    <div class="item l3"><h3>A LA CARTE - 25 €&nbsp; MATT PRINTS</h3><p>Each print is professionally edited, printed on archival photo paper.<br>Purchase includes the JPEG file for your personal digital use.<br>20x30 cm and Smaller</p></div>
    <div class="item r1"><h3>A LA CARTE - 45 €&nbsp;&nbsp;&nbsp; ASHFIELD PRINTS</h3><p>Prints on Ashfield (watercolor) paper are Clara's favorite for large format color prints 30x40 cm</p></div>
    <div class="item r2"><h3>A LA CARTE - 100 €&nbsp;&nbsp;&nbsp; CANVAS PRINTS</h3><p>Ready-to-hang, stretched canvas wall art of your favorite images<br>30x40 cm</p></div>
    <div class="item r3"><h3>A LA CARTE - 350 €&nbsp;&nbsp;&nbsp; FRAMED + MATTED PRINTS</h3><p>Beautiful Ashfield prints finished with wide mats and simple, elegant frames of your choice 30x40 inch</p></div>
    <div class="item r4"><h3>PRICES BEGIN AT - 100 €<br>CUSTOM DESIGNED ALBUMS</h3><p>Images from your session are selected for the custom design of an album and bound in a book for a modern presentation of your images. There are a number of cover choices for the classic flush-mount and beautifully crafted albums. A great way to display all of your favorite images from your session on your coffee table.</p></div>
    <div class="bubbles-dark bottom" role="img" aria-label="Decorative band of translucent bubbles"></div>
  </section>
  <div class="label" style="left:602px;top:811px">INSIDE PAGE 2</div>

</div>
</body>
</html>
```